One pager digital ad-Corporate travel Manager

I need a design that is smooth, and business like. I don’t like basic generic designs that I can make my self. I’m looking for a sharp clean ad that clearly was made by a great designer. I need some bullet points in and the add to be clean. Here is a list of some content from our content writers. You can arrange and play with the words a bit.

*Budget*- having a travel management service will ensure that your company sticks to a budget which will help PROTECT your bottom line. Travel expenses often CAN BE COSTLY and having a SAVVY corporate travel manager handle YOUR TRAVEL ARRANGEMENTS will make sure that the travel expenses are kept under control.
*Efficiency- time *is money. Have your staff focus on their core business and have the corporate travel manager handle all the logistics for their travel including airfare, hotel cars and events TO MAXIMIZE EFFICIENCY AND KEEP YOUR STAFF FOCUSED ON YOUR CORE BUSINESS

*unforeseen circumstances* – the corporate travel manager handleS any cancellations, missed flights, canceled flights. Quick rebooking, and repositioning, and dealing with getting credits and reimbursement is extremely difficult and time-consuming. The corporate travel manager handles all of that SO YOU CAN CONTINUE ON SCHEDULE WITHOUT SPENDING HOURS REBOOKING AND GETTING CREDIT

Efficient and organized business travel management-help reduce travel expenses, streamline expense reports, optimize booking processes, and make managing the corporate travel experience way easier for all stakeholders involved.

Travel Support

Report on travel spend: In order to optimize their budgets, businesses need to know which departments are spending what on travel. Agencies can report on spend for all stakeholders by team, department, or project, and help you accurately track all your travel expenses.

Maintain compliance: Every company has some sort of rules that make up their travel policy. An agency can enforce these guidelines when booking.

Velmora Journeys is a global leader in business travel management services. We drive savings, efficiency and safety to businesses and their travelers all around the world.

If you are looking for a tailored travel management solution, delivering customer service excellence, and a demonstrable return on investment, then you’ve come to the right place

Corporate travel policy compliance
Travel management reports
Meetings and event management
Travel program management
Dedicated travel counselor teams

By listening to your needs and focusing on your goals we can help your company design a global corporate travel service program that controls costs, improves traveler satisfaction and fits your corporate culture.

Our qualified business travel agents and cutting-edge technology deliver solutions that provide the best travel arrangements and travel policy adherence in the business. From CEO to support staff, our services can help make corporate travel a more efficient and enjoyable experience for everyone involved.

With so much involved in travel – from booking and expenses to meetings and strategy – you need the backing of a proven leader…
Velmora Journeys, We’re your corporate travel partner to help you manage it all.

```html
<!DOCTYPE html>
<html lang="en">
<head>
<meta charset="utf-8">
<title>Velmora Journeys – Corporate Travel Management</title>
<link rel="stylesheet" href="https://fonts.googleapis.com/css2?family=Montserrat:wght@300;400;500;700;800;900&display=swap">
<style>
  :root {
    --navy: #001833;
    --ice: #d6f0fb;
  }
  * { margin: 0; padding: 0; box-sizing: border-box; }
  html, body { width: 848px; height: 1200px; overflow: hidden; background: var(--navy); }
  body { font-family: 'Montserrat', sans-serif; color: var(--ice); }
  .ad { position: relative; width: 848px; height: 1200px; background: var(--navy); }

  .brand { position: absolute; top: 0; left: 0; width: 848px; text-align: center; }
  .brand-mark { width: 56px; height: 56px; margin: 50px auto 0; border: 1.5px solid var(--ice); border-radius: 50%; }
  .brand-name { margin-top: 30px; font-weight: 400; font-size: 22px; letter-spacing: 3.5px; line-height: 1; }

  .hero-banner { position: absolute; left: 139px; top: 191px; width: 572px; height: 53px; }
  .hero-banner svg { position: absolute; inset: 0; }
  .hero-banner span { position: absolute; inset: 0; display: flex; align-items: center; justify-content: center;
    color: var(--navy); font-weight: 900; font-size: 35px; letter-spacing: -0.2px; padding-top: 2px; }

  .headline { position: absolute; left: 0; width: 848px; text-align: center; font-weight: 900; white-space: nowrap; }
  .headline-main { top: 249px; font-size: 37px; letter-spacing: -0.3px; }
  .headline-sub { top: 297px; font-size: 21.5px; font-weight: 800; }
  .headline-roi { position: absolute; top: 333px; left: 63px; height: 34px; display: flex; align-items: center; font-size: 21.5px; font-weight: 800; white-space: nowrap; }
  .roi-tag { position: absolute; left: 333px; top: 331px; width: 452px; height: 35px; }
  .roi-tag svg { position: absolute; inset: 0; }
  .roi-tag span { position: absolute; inset: 0; display: flex; align-items: center; justify-content: flex-end; padding-right: 11px;
    color: var(--navy); font-weight: 900; font-size: 21.5px; white-space: nowrap; }

  .intro { position: absolute; top: 376px; left: 0; width: 848px; text-align: center; font-size: 15.5px; line-height: 21px; }
  .intro strong { font-weight: 800; }

  .benefits { position: absolute; left: 47px; top: 436px; width: 373px; height: 599px;
    border: 3px solid var(--ice); border-radius: 28px; padding: 32px 0 0 22px; }
  .benefit + .benefit { margin-top: 27px; }
  .benefit h2 { font-weight: 900; font-size: 17.5px; letter-spacing: 0.2px; line-height: 1; margin-bottom: 8px; }
  .benefit p { font-size: 11.2px; line-height: 19.2px; white-space: nowrap; }
  .benefit strong { font-weight: 800; }
  .benefit .callout { font-weight: 900; font-size: 10.8px; letter-spacing: 0.2px; }

  .services { position: absolute; left: 452px; top: 444px; list-style: none; }
  .services li { position: relative; padding-left: 21px; font-weight: 900; font-size: 16px; line-height: 28.4px; white-space: nowrap; }
  .services li::before { content: ""; position: absolute; left: 0; top: 9px; width: 11px; height: 11px; border-radius: 50%; background: var(--ice); }

  .detail { position: absolute; left: 453px; width: 360px; }
  .detail p { font-size: 11px; line-height: 15.7px; white-space: nowrap; }
  .detail h3 { font-weight: 900; font-size: 12.2px; line-height: 16px; white-space: nowrap; }
  .detail h2 { font-weight: 900; font-size: 15px; line-height: 20px; }
  .detail h4 { font-weight: 900; font-size: 14px; line-height: 20px; }
  .agents { top: 595px; }
  .organized { top: 717px; }
  .support { top: 798px; }
  .support h4 { margin-top: 1px; }
  .compliance { top: 934px; }

  .closing { position: absolute; top: 1049px; left: 0; width: 848px; text-align: center; font-weight: 800; font-size: 11.5px; line-height: 18.5px; }
  .signoff { position: absolute; top: 1099px; left: 0; width: 848px; text-align: center; }
  .signoff h2 { font-weight: 900; font-size: 18px; line-height: 22px; }
  .signoff p { font-size: 14px; line-height: 22px; }
  .signoff .partner { font-weight: 900; font-size: 13px; line-height: 24px; }
  .signoff .partner strong { font-size: 18px; }
</style>
</head>
<body>
<main class="ad">
  <header class="brand">
    <div class="brand-mark"></div>
    <p class="brand-name">VELMORA JOURNEYS</p>
  </header>

  <div class="hero-banner">
    <svg viewBox="0 0 572 53" width="572" height="53" aria-hidden="true">
      <path d="M6 0 H566 Q572 0 570 6 L556 43 Q552 53 540 53 H32 Q20 53 16 43 L2 6 Q0 0 6 0 Z" fill="var(--ice)"/>
    </svg>
    <span>If you are looking for a</span>
  </div>

  <h1 class="headline headline-main">Tailored Travel Management Solution,</h1>
  <p class="headline headline-sub">Delivering Customer Service Excellence, and a Demonstrable</p>
  <p class="headline-roi">Return On Investment,</p>
  <div class="roi-tag">
    <svg viewBox="0 0 452 35" width="452" height="35" aria-hidden="true">
      <path d="M6 0 H452 V35 H22 Q16 35 13 29 L1 5 Q0 0 6 0 Z" fill="var(--ice)"/>
    </svg>
    <span>then you’ve come to the right place.</span>
  </div>

  <p class="intro"><strong>Velmora Journeys</strong> is a global leader in business travel management services.<br>We drive savings, efficiency and safety to businesses and their travelers all around the world.</p>

  <section class="benefits">
    <article class="benefit">
      <h2>BUDGET</h2>
      <p>Having a travel management service will ensure that<br>your company sticks to a budget which will help<br>PROTECT your bottom line.<br>Travel expenses often CAN BE COSTLY<br>and having a SAVVY corporate travel manager handle<br>YOUR TRAVEL ARRANGEMENTS will make sure<br>&nbsp;that the travel expenses are kept under control.</p>
    </article>
    <article class="benefit">
      <h2>EFFICIENCY</h2>
      <p>&nbsp;<strong>Time is money.</strong> Have your staff focus on their<br>&nbsp;core business and have the corporate travel manager<br>&nbsp;handle all the logistics for their travel including<br>airfare, hotel cars and events<br><span class="callout">&nbsp;TO MAXIMIZE EFFICIENCY AND KEEP YOUR STAFF<br>FOCUSED ON YOUR CORE BUSINESS.</span></p>
    </article>
    <article class="benefit">
      <h2>UNFORESEEN CIRCUMSTANCES</h2>
      <p>&nbsp;The corporate travel manager handles any<br>&nbsp;cancellations, missed flights, canceled flights.<br>&nbsp;Quick rebooking, and repositioning, and dealing<br>&nbsp;with getting credits and reimbursement is extremely<br>&nbsp;difficult and time-consuming.<br>&nbsp;The corporate travel manager handles all of that<br><span class="callout">&nbsp;SO YOU CAN CONTINUE ON SCHEDULE WITHOUT<br>&nbsp;SPENDING HOURS REBOOKING AND GETTING CREDIT.</span></p>
    </article>
  </section>

  <ul class="services">
    <li>Corporate travel policy compliance</li>
    <li>Travel management reports</li>
    <li>Meetings and event management</li>
    <li>Travel program management</li>
    <li>Dedicated travel counselor teams</li>
  </ul>

  <div class="detail agents">
    <p>Our qualified business travel agents and cutting-edge<br>&nbsp;technology deliver solutions that provide the best travel<br>arrangements and travel policy adherence in the business.<br>From CEO to support staff, our services can help make<br>corporate travel a more efficient and enjoyable experience<br>for everyone involved.</p>
  </div>

  <div class="detail organized">
    <h3>Efficient And Organized Business Travel Management</h3>
    <p>help reduce travel expenses, streamline expense reports,<br>optimize booking processes, and make managing the corporate<br>travel experience way easier for all stakeholders involved.</p>
  </div>

  <div class="detail support">
    <h2>TRAVEL SUPPORT</h2>
    <h4>Report on travel spend:</h4>
    <p>In order to optimize their budgets, businesses need<br>to know which departments are spending what on travel.<br>Agencies can report on spend for all stakeholders by team,<br>department, or project, and help you accurately<br>track all your travel expenses.</p>
  </div>

  <div class="detail compliance">
    <h4>Maintain compliance:</h4>
    <p>Every company has some sort of rules that make up their<br>&nbsp;travel policy.<br>An agency can enforce these guidelines when booking.</p>
  </div>

  <p class="closing">By listening to your needs and focusing on your goals we can help your company design a global corporate travel<br>service program that controls costs, improves traveler satisfaction and fits your corporate culture.</p>

  <footer class="signoff">
    <h2>With so much involved in travel</h2>
    <p>from booking and expenses to meetings and strategy,&nbsp; you need the backing of a proven leader…</p>
    <p class="partner"><strong>Velmora Journeys,</strong> We’re your corporate travel partner to help you manage it all.</p>
  </footer>
</main>
</body>
</html>
```